Breezeway Climate Business Card Design

Design new, 2 sides, business cards for a residential and light commercial heating, air conditioning contractor.

Target Market(s)

Homeowners, small businesses

Industry/Entity Type

Business

Contact Information for Business Card

Dominic Vasquerelli
Phone - 555-214-6837
Email
Address - PO box 618
Millbrook NJ 07999
Website - www.BreezewayClimateLLC.example

Requirements
Must have
• logo, company colors, standard size with no die cut, so I can use printhaven

```html
<!DOCTYPE html>
<html lang="en">
<head>
<meta charset="utf-8">
<title>Breezeway Climate Business Card</title>
<link rel="stylesheet" href="https://fonts.googleapis.com/css2?family=Open+Sans:wght@400;600;700&display=swap">
<style>
  :root {
    --backdrop: #d9d6d3;
    --card-white: #fbfbfa;
    --card-black: #141414;
    --ink: #222222;
    --ink-soft: #3a3a3a;
    --paper-light: #e9e9e7;
  }
  * { box-sizing: border-box; margin: 0; padding: 0; }
  html, body {
    width: 1200px;
    height: 844px;
    overflow: hidden;
    background: var(--backdrop);
    font-family: "Open Sans", Arial, sans-serif;
  }
  .card-sheet {
    position: relative;
    width: 1200px;
    height: 844px;
  }
  .card {
    position: absolute;
    top: 267px;
    width: 540px;
    height: 310px;
    box-shadow: 0 6px 18px rgba(0,0,0,0.18);
  }
  .card-front { left: 40px; background: var(--card-white); color: var(--ink); }
  .card-back  { left: 620px; background: var(--card-black); color: var(--paper-light); }

  .brand {
    display: flex;
    align-items: center;
    gap: 10px;
    font-weight: 700;
    font-size: 22px;
    letter-spacing: 0.5px;
    text-transform: uppercase;
    white-space: nowrap;
  }
  .brand-dot {
    width: 16px;
    height: 16px;
    border-radius: 50%;
    background: currentColor;
    flex: none;
  }
  .card-front .brand { position: absolute; top: 52px; right: 36px; color: var(--ink); }
  .card-back .brand {
    position: absolute;
    top: 50%;
    left: 50%;
    transform: translate(-50%, -50%);
    font-size: 26px;
    color: var(--paper-light);
  }

  .contact-block {
    position: absolute;
    left: 36px;
    top: 118px;
    color: var(--ink-soft);
  }
  .person-name { font-size: 18px; font-weight: 700; color: var(--ink); line-height: 1.2; }
  .person-title { font-size: 13.5px; line-height: 1.3; margin-bottom: 10px; }
  .postal-address { font-size: 13.5px; line-height: 1.35; margin-bottom: 8px; padding-left: 10px; }
  .contact-list { list-style: none; font-size: 13.5px; line-height: 1.4; padding-left: 20px; }
  .contact-list li { display: flex; align-items: center; gap: 10px; }
  .contact-icon { width: 12px; height: 12px; flex: none; fill: var(--ink-soft); }
</style>
</head>
<body>
<main class="card-sheet">
  <section class="card card-front" aria-label="Business card front">
    <div class="brand"><span class="brand-dot"></span>Breezeway Climate</div>

    <div class="contact-block">
      <p class="person-name">Dominic Vasquerelli</p>
      <p class="person-title">Managing Director</p>
      <p class="postal-address">PO box 618<br>Millbrook NJ 07999</p>
      <ul class="contact-list">
        <li>
          <svg class="contact-icon" viewBox="0 0 12 12" aria-hidden="true"><path d="M2.5 1 L4.5 1 L5.2 3.6 L4 4.6 C4.7 6 6 7.3 7.4 8 L8.4 6.8 L11 7.5 L11 9.5 C11 10.3 10.3 11 9.5 11 C5 11 1 7 1 2.5 C1 1.7 1.7 1 2.5 1 Z"/></svg>
          <span>555-214-6837</span>
        </li>
        <li>
          <svg class="contact-icon" viewBox="0 0 12 12" aria-hidden="true"><path d="M4 2 L8 2 L8 3.5 L11 3.5 L11 10.5 L1 10.5 L1 3.5 L4 3.5 Z M5 3 L5 3.5 L7 3.5 L7 3 Z"/></svg>
          <span>555-214-6838</span>
        </li>
        <li>
          <svg class="contact-icon" viewBox="0 0 12 12" aria-hidden="true"><path d="M1 2.5 L11 2.5 L11 9.5 L1 9.5 Z M1.6 3 L6 6.4 L10.4 3 Z" fill-rule="evenodd"/></svg>
          <span>info@breezewayclimate.example</span>
        </li>
        <li>
          <svg class="contact-icon" viewBox="0 0 12 12" aria-hidden="true"><circle cx="6" cy="6" r="5"/><path d="M1 6 H11 M6 1 C3.8 3.5 3.8 8.5 6 11 M6 1 C8.2 3.5 8.2 8.5 6 11" stroke="#fbfbfa" stroke-width="0.8" fill="none"/></svg>
          <span>www.BreezewayClimateLLC.example</span>
        </li>
      </ul>
    </div>
  </section>

  <section class="card card-back" aria-label="Business card back">
    <div class="brand"><span class="brand-dot"></span>Breezeway Climate</div>
  </section>
</main>
</body>
</html>
```